Pillow Company needs Pillow Insert Design

I just started a new pillow line with two pillow types. I have a hotel pillow and an organic pillow. I need two pillow insert signs designed that follow the same layout but are different color types. I want one sign to incorporate silver and white look and another sign to incorporate a green and white look (this one to look organic). They must have the same layout but different colors. I have include examples of what I want it to look like. In addition, I have uploaded the two hi res images for each sign. My logo is uploaded too.

I am open to other concepts and colors as long as it looks modern, clean and upscale. In addition, I need a Made in the USA logo on the pillow insert designs.

I have attached details on sign, images to be used, and examples that I like.

The Pillow Sign Size is 12 inches x 12 inches.

```html
<!DOCTYPE html>
<html lang="en">
<head>
<meta charset="utf-8">
<title>Lunaris Luxury Pillow Insert</title>
<link href="https://fonts.googleapis.com/css2?family=Great+Vibes&family=Dancing+Script:wght@500&family=Roboto+Condensed:wght@400&family=Roboto:wght@500&display=swap" rel="stylesheet">
<style>
  :root {
    --sheet-light: #f4f6f9;
    --sheet-mid: #dfe4ea;
    --sheet-shadow: #c9d0d9;
    --slate-dark: #56626c;
    --slate-light: #8c979f;
    --ink: #2f3540;
    --ink-soft: #3d4450;
    --script-grey: #6b7178;
    --brand-green: #5cb83a;
    --bullet: #7d848c;
    --panel-white: rgba(255,255,255,0.72);
    --panel-grey: rgba(214,220,228,0.55);
  }
  html, body { margin: 0; padding: 0; overflow: hidden; }
  body { width: 1200px; height: 1200px; }
  .insert {
    position: relative;
    width: 1200px;
    height: 1200px;
    overflow: hidden;
    background: linear-gradient(180deg, var(--sheet-light) 0%, var(--sheet-mid) 55%, var(--sheet-light) 80%, #e7ebf0 100%);
    font-family: "Roboto Condensed", "Arial Narrow", sans-serif;
    color: var(--ink);
  }
  .hero-photo {
    position: absolute;
    left: 0; top: 0;
    width: 1200px; height: 680px;
    background:
      radial-gradient(ellipse 420px 260px at 560px 380px, rgba(224,190,165,0.55), transparent 70%),
      radial-gradient(ellipse 260px 200px at 780px 420px, rgba(156,190,224,0.55), transparent 70%),
      radial-gradient(ellipse 240px 180px at 350px 430px, rgba(190,196,204,0.6), transparent 70%),
      linear-gradient(180deg, #eef1f5 0%, #f7f8fa 45%, rgba(244,246,249,0) 100%);
  }
  .brand {
    position: absolute;
    left: 40px; top: 50px;
    display: flex; align-items: center; gap: 22px;
  }
  .brand-square {
    width: 110px; height: 110px;
    background: var(--brand-green);
  }
  .brand-name {
    font-family: "Roboto", Arial, sans-serif;
    font-weight: 500;
    font-size: 68px;
    color: var(--brand-green);
    letter-spacing: -0.5px;
  }
  .origin-badge {
    position: absolute;
    left: 1038px; top: 24px;
    width: 130px; height: 86px;
    background: #ffffff;
    border: 2px solid #d7dbe0;
    box-sizing: border-box;
  }
  .luxury-band {
    position: absolute;
    left: 0; top: 552px;
    width: 584px; height: 218px;
    background: linear-gradient(90deg, var(--slate-light) 0%, var(--slate-dark) 100%);
  }
  .luxury-title {
    position: absolute;
    left: 78px; top: 530px;
    font-family: "Great Vibes", cursive;
    font-size: 196px;
    line-height: 1;
    color: #ffffff;
  }
  .intro-panel {
    position: absolute;
    left: 584px; top: 564px;
    width: 616px; height: 192px;
    background: var(--panel-white);
  }
  .intro-text {
    position: absolute;
    left: 626px; top: 604px;
    margin: 0;
    font-size: 29px;
    line-height: 38px;
    color: var(--ink-soft);
  }
  .features-panel {
    position: absolute;
    left: 536px; top: 774px;
    width: 664px; height: 282px;
    background: var(--panel-grey);
  }
  .feature-list {
    position: absolute;
    left: 572px; top: 796px;
    margin: 0; padding: 0;
    list-style: none;
    font-size: 20px;
    line-height: 35.6px;
    color: var(--ink);
  }
  .feature-list li { display: flex; align-items: center; gap: 14px; }
  .feature-list li::before {
    content: "";
    width: 11px; height: 11px;
    background: var(--bullet);
    flex: none;
  }
  .materials-text {
    position: absolute;
    left: 30px; top: 820px;
    width: 444px;
    margin: 0;
    text-align: right;
    font-size: 21px;
    line-height: 32px;
    color: var(--ink);
  }
  .tagline {
    position: absolute;
    left: 0; top: 1082px;
    width: 1200px;
    margin: 0;
    text-align: center;
    font-family: "Dancing Script", cursive;
    font-weight: 500;
    font-size: 56px;
    color: var(--script-grey);
    line-height: 1;
  }
  .made-line {
    position: absolute;
    left: 0; top: 1150px;
    width: 1200px;
    margin: 0;
    text-align: center;
    font-size: 25px;
    color: var(--script-grey);
  }
</style>
</head>
<body>
<div class="insert">
  <div class="hero-photo" role="img" aria-label="Smiling family of three relaxing together in a bed with white pillows and sheets"></div>

  <div class="brand">
    <div class="brand-square"></div>
    <span class="brand-name">Lunaris</span>
  </div>

  <div class="origin-badge" aria-label="Made in USA badge"></div>

  <div class="luxury-band"></div>
  <div class="luxury-title">Luxury</div>

  <div class="intro-panel"></div>
  <p class="intro-text">This pillow was designed to give you the<br>most comfortable night’s sleep.<br>Designed for all types of sleep positions.</p>

  <p class="materials-text">We added revolutionary features from our advanced Super Soft Premium Memory Foam that has an open cell structure design that recovers quickly and does not trap heat to our gel infused polyester fiber to our temperature managing Veluna Fabric.</p>

  <div class="features-panel"></div>
  <ul class="feature-list">
    <li>Made From the Finest Premium Materials</li>
    <li>Adjusts to your Body Weight and Temperature</li>
    <li>Ventilated and Does Not Trap Heat</li>
    <li>Cool Non-Allergenic, Anti-Microbial, and Hypoallergenic</li>
    <li>Conforms to Head and Neck for optimal Alignment during Sleep</li>
    <li>Mildew Proof and Dust Mite Resistant</li>
    <li>PureFoam Standard toxin free certified foam</li>
  </ul>

  <p class="tagline">Surround Yourself with the Best!</p>
  <p class="made-line">Individually Handcrafted and Made in USA</p>
</div>
</body>
</html>
```